Need UI design for an iOS app game with most of the layout planned

The name of the game is "QUADRIX".

The goal of the game is to find a way to manipulate four numbers so that the end result is 24. Addition, subtraction, multiplication and division may be used and each number can only be used once.

The list of items we need is:

1. launch image, app icon, UI design of all scenes (10-12 scenes) of the app.
2. App background image should support screen size of both 640x1136.
3. Files are preferred to be in (.eps) format so that resolution can be adjusted later. But other file formats are welcome as long as resolution is high enough.
4. Icons, buttons, background image etc. should have their own file so that later they can be moved around in case design is changed.

The detailed requirement is in the attached file. The actual layout can vary if it can help achieve better result. We also attached several screenshots from iOS game "Glimbo". You can use that as your reference.

```html
<!DOCTYPE html>
<html lang="en">
<head>
<meta charset="utf-8">
<title>QUADRIX – Number Tile States</title>
<link rel="stylesheet" href="https://fonts.googleapis.com/css2?family=Lato:wght@400&display=swap">
<style>
  :root {
    --canvas-bg: #ffffff;

    --plain-top: #f7f7f7;
    --plain-mid: #e8e8e8;
    --plain-low: #f4f4f4;
    --plain-shade: #c4c4c4;
    --plain-edge: #4a4a4a;

    --blue-top: #29a9e1;
    --blue-mid: #2299d6;
    --blue-low: #1b75bc;
    --blue-edge: #232b33;
    --blue-frame: #1c75bc;

    --amber-top: #fbb040;
    --amber-mid: #f9a533;
    --amber-low: #f7941d;
    --amber-edge: #3a2a18;
    --amber-frame: #f15a29;

    --digit-dark: #111111;
    --digit-light: #ffffff;
  }

  * { box-sizing: border-box; margin: 0; padding: 0; }

  html, body {
    width: 1200px;
    height: 675px;
    overflow: hidden;
    background: var(--canvas-bg);
  }

  .tile-sheet {
    position: relative;
    width: 1200px;
    height: 675px;
  }

  .tile {
    position: absolute;
    display: flex;
    align-items: center;
    justify-content: center;
    border-radius: 8px;
    font-family: "Lato", sans-serif;
    font-weight: 400;
    font-size: 50px;
    line-height: 1;
    color: var(--digit-dark);
    overflow: hidden;
  }

  .tile--large { width: 104px; height: 104px; }
  .tile--small { width: 92px; height: 92px; }

  .tile--plain {
    background: linear-gradient(to bottom,
      var(--plain-top) 0%, var(--plain-mid) 25%, var(--plain-low) 88%,
      var(--plain-shade) 93%, var(--plain-edge) 100%);
  }
  .tile--blue {
    background: linear-gradient(to bottom,
      var(--blue-top) 0%, var(--blue-top) 42%, var(--blue-mid) 62%,
      var(--blue-low) 88%, var(--blue-edge) 100%);
  }
  .tile--amber {
    background: linear-gradient(to bottom,
      var(--amber-top) 0%, var(--amber-top) 45%, var(--amber-mid) 66%,
      var(--amber-low) 88%, var(--amber-edge) 100%);
  }

  .tile--plain.frame-thin, .tile--blue.frame-thin { border: 3px solid var(--blue-frame); }
  .tile--plain.frame-thick, .tile--blue.frame-thick { border: 6px solid var(--blue-frame); }
  .tile--amber.frame-thin { border: 3px solid var(--amber-frame); }
  .tile--amber.frame-thick { border: 6px solid var(--amber-frame); }

  .digit--light { color: var(--digit-light); }

  .row-blank { top: 48px; }
  .row-one   { top: 197px; }
  .row-two   { top: 320px; }
  .row-three { top: 443px; }
  .row-four  { top: 569px; }

  .tile--large.col-1 { left: 31px; }
  .tile--large.col-2 { left: 159px; }
  .tile--large.col-3 { left: 287px; }
  .tile--large.col-4 { left: 418px; }
  .tile--large.col-5 { left: 546px; }
  .tile--large.col-6 { left: 673px; }
  .tile--large.col-7 { left: 805px; }
  .tile--large.col-8 { left: 933px; }
  .tile--large.col-9 { left: 1060px; }

  .tile--small.col-1 { left: 40px; }
  .tile--small.col-2 { left: 156px; }
  .tile--small.col-3 { left: 285px; }
  .tile--small.col-4 { left: 416px; }
  .tile--small.col-5 { left: 546px; }
  .tile--small.col-6 { left: 675px; }
  .tile--small.col-7 { left: 806px; }
  .tile--small.col-8 { left: 935px; }
  .tile--small.col-9 { left: 1064px; }
</style>
</head>
<body>
<main class="tile-sheet" aria-label="QUADRIX number tile states">
  <div class="tile tile--large tile--plain row-blank col-1"></div>
  <div class="tile tile--large tile--plain frame-thin row-blank col-2"></div>
  <div class="tile tile--large tile--plain frame-thick row-blank col-3"></div>
  <div class="tile tile--large tile--blue row-blank col-4"></div>
  <div class="tile tile--large tile--blue frame-thin row-blank col-5"></div>
  <div class="tile tile--large tile--blue frame-thick row-blank col-6"></div>
  <div class="tile tile--large tile--amber row-blank col-7"></div>
  <div class="tile tile--large tile--amber frame-thin row-blank col-8"></div>
  <div class="tile tile--large tile--amber frame-thick row-blank col-9"></div>

  <div class="tile tile--small tile--plain row-one col-1">1</div>
  <div class="tile tile--small tile--plain frame-thin row-one col-2">1</div>
  <div class="tile tile--small tile--plain frame-thick row-one col-3">1</div>
  <div class="tile tile--small tile--blue row-one col-4">1</div>
  <div class="tile tile--small tile--blue frame-thin row-one col-5">1</div>
  <div class="tile tile--small tile--blue frame-thick row-one col-6">1</div>
  <div class="tile tile--small tile--amber row-one col-7">1</div>
  <div class="tile tile--small tile--amber frame-thin row-one col-8">1</div>
  <div class="tile tile--small tile--amber frame-thick row-one col-9">1</div>

  <div class="tile tile--small tile--plain row-two col-1">2</div>
  <div class="tile tile--small tile--plain frame-thin row-two col-2">2</div>
  <div class="tile tile--small tile--plain frame-thick row-two col-3">2</div>
  <div class="tile tile--small tile--blue row-two col-4">2</div>
  <div class="tile tile--small tile--blue frame-thin row-two col-5">2</div>
  <div class="tile tile--small tile--blue frame-thick row-two col-6">2</div>
  <div class="tile tile--small tile--amber row-two col-7">2</div>
  <div class="tile tile--small tile--amber frame-thin row-two col-8">2</div>
  <div class="tile tile--small tile--amber frame-thick row-two col-9">2</div>

  <div class="tile tile--small tile--plain row-three col-1">3</div>
  <div class="tile tile--small tile--plain frame-thin row-three col-2">3</div>
  <div class="tile tile--small tile--plain frame-thick row-three col-3">3</div>
  <div class="tile tile--small tile--blue digit--light row-three col-4">3</div>
  <div class="tile tile--small tile--blue frame-thin digit--light row-three col-5">3</div>
  <div class="tile tile--small tile--blue frame-thick digit--light row-three col-6">3</div>
  <div class="tile tile--small tile--amber digit--light row-three col-7">3</div>
  <div class="tile tile--small tile--amber frame-thin digit--light row-three col-8">3</div>
  <div class="tile tile--small tile--amber frame-thick digit--light row-three col-9">3</div>

  <div class="tile tile--small tile--plain row-four col-1">4</div>
  <div class="tile tile--small tile--plain frame-thin row-four col-2">4</div>
  <div class="tile tile--small tile--plain frame-thick row-four col-3">4</div>
  <div class="tile tile--small tile--blue digit--light row-four col-4">4</div>
  <div class="tile tile--small tile--blue frame-thin digit--light row-four col-5">4</div>
  <div class="tile tile--small tile--blue frame-thick digit--light row-four col-6">4</div>
  <div class="tile tile--small tile--amber digit--light row-four col-7">4</div>
  <div class="tile tile--small tile--amber frame-thin digit--light row-four col-8">4</div>
  <div class="tile tile--small tile--amber frame-thick digit--light row-four col-9">4</div>
</main>
</body>
</html>
```